Design a Website Mockup for Rural Water Company

We are looking for a website design for a rural drinking water company. The site will be implemented in WordPress. We need a homepage, a subpage, and a contact us page design.
*** NOTE: This is for the design in Photoshop only - we will handle the conversion to HTML / WordPress **
The company provides drinking water hookup to homes in a rural farm area in the US. Good visual elements might be rolling farm land combined with drinking water and other water related imagery.
Required elements include:
- Navigation (Home, News, New Customer, Resources, Rates, Rules and Regs, Board and Staff, Pay Online, Contact Us)
- News items / updates
- A "Water Facts" rotator
- A content/image rotator on the homepage
- A "Make Payment Online" button / link
I've attached a screenshot of another rural water company's website that will have similar pages. I've also attached a potential home page layout.
We will need the design as a layered PSD.

```html
<!DOCTYPE html>
<html lang="en">
<head>
<meta charset="utf-8">
<title>Cedar Ridge Water District</title>
<link rel="stylesheet" href="https://fonts.googleapis.com/css2?family=Arimo:wght@400;700&display=swap">
<style>
:root{
  --navy:#0b2a66;
  --navy-deep:#061c4d;
  --blue:#1e6fc4;
  --sky:#2f9fe6;
  --lime:#8fd13a;
  --green:#4aa524;
  --panel:#dcebfa;
  --panel-line:#b9d3ee;
  --text:#3b3b3b;
  --link:#1c73c9;
  --page:#ffffff;
  --hero:#9fc2d6;
}
*{box-sizing:border-box;margin:0;padding:0}
html,body{width:1200px;height:907px;overflow:hidden}
body{font-family:"Arimo",Arial,sans-serif;color:var(--text);position:relative;background:#cfe6f6}
.backdrop{position:absolute;inset:0;background:
  radial-gradient(ellipse 260px 420px at 60px 260px,rgba(70,150,215,.55),transparent 70%),
  radial-gradient(ellipse 260px 380px at 1150px 160px,rgba(70,150,215,.5),transparent 70%),
  radial-gradient(ellipse 700px 120px at 600px 900px,rgba(60,140,210,.45),transparent 70%),
  linear-gradient(180deg,#e4f2fb 0%,#bcdcf1 100%)}
.page{position:absolute;left:165px;top:0;width:855px;height:864px;background:var(--page);box-shadow:0 0 12px rgba(0,40,90,.25)}
.abs{position:absolute}
.masthead{left:200px;top:0;width:784px;height:111px;background:linear-gradient(180deg,var(--navy-deep),#0d3580);color:#fff}
.brand{left:22px;top:26px;font-size:32px;font-weight:700;letter-spacing:-.3px}
.tagline{left:22px;top:66px;font-size:16px;color:#5fb4ee}
.phone{right:24px;top:34px;font-size:22px;font-weight:700}
.phone span{color:var(--lime)}
.address{right:24px;top:70px;font-size:12.5px;color:#5fb4ee}
.nav{left:200px;top:129px;width:191px;list-style:none}
.nav li{height:30px;line-height:30px;padding-left:23px;font-size:16px;color:#fff;background:linear-gradient(180deg,#0e3a86,var(--navy-deep));border-bottom:1px solid #2a5aa8}
.nav li.current{background:linear-gradient(180deg,#3ab0f0,#1b7fd0);position:relative}
.nav li.current svg{position:absolute;right:0;top:0}
.slider{left:408px;top:129px;width:576px;height:271px}
.slide-photo{position:absolute;left:0;top:0;width:576px;height:248px;background:var(--hero)}
.slide-caption{position:absolute;left:301px;top:55px;width:248px;height:133px;background:rgba(240,246,252,.95);box-shadow:0 1px 4px rgba(0,0,0,.25);padding:18px 22px}
.slide-caption h2{font-size:21px;color:var(--navy)}
.slide-caption h2 span{color:var(--blue)}
.slide-caption p{margin-top:14px;font-size:13px;font-weight:700;color:#111;line-height:16px}
.slide-bar{position:absolute;left:0;top:248px;width:576px;height:23px;background:var(--blue)}
.dot{position:absolute;top:8px;width:7px;height:7px;border-radius:50%;background:#fff}
.facts{left:201px;top:444px;width:190px;height:216px;background:linear-gradient(180deg,#c9e2f6,var(--panel));border:1px solid var(--panel-line);padding:40px 20px 0 22px}
.facts h3{font-size:16px;color:var(--navy)}
.facts p{margin-top:12px;font-size:12.5px;line-height:16.2px;color:#444}
.member{left:201px;top:671px;width:190px;height:86px;border:1px solid var(--panel-line);padding:7px 18px}
.member em{font-size:12px;color:#b07a10}
.badge{position:absolute;background:#e3ecf6;border:1px solid #9fb6d3}
.welcome{left:407px;top:438px;width:362px}
.welcome h1{font-size:27px;color:var(--navy)}
.welcome p{margin-top:22px;font-size:12.5px;line-height:16.2px;color:#444}
.btn{left:793px;width:191px;height:47px;border-radius:4px;color:#fff;font-size:22px;font-weight:700;text-align:center;line-height:45px;text-shadow:0 1px 2px rgba(0,0,0,.45);box-shadow:2px 3px 4px rgba(0,0,0,.35)}
.btn-pay{top:444px;background:linear-gradient(180deg,#2f7fd6,#0c3f95)}
.btn-new{top:503px;background:linear-gradient(180deg,#7bc943,var(--green))}
.news{left:795px;top:569px;width:189px;height:188px;border:1px solid var(--panel-line)}
.news h3{height:30px;line-height:30px;padding-left:18px;font-size:16px;color:var(--navy);background:var(--panel);border-bottom:1px solid var(--panel-line)}
.news-item{padding:10px 8px 0 18px;border-bottom:1px solid var(--panel-line);font-size:11px;line-height:13px;color:#444}
.news-item.tall{height:61px}
.news-item.short{height:44px}
.news-item:last-child{border-bottom:0}
.news-item time{display:block;color:var(--link)}
.all-news{left:793px;top:767px;font-size:11.5px;color:#555;text-decoration:underline}
.footer{left:165px;top:813px;width:855px;height:51px;background:linear-gradient(180deg,#0d3580,var(--navy-deep));color:#7ec6f2;font-size:13px;text-align:center;line-height:51px}
</style>
</head>
<body>
<div class="backdrop" role="img" aria-label="Splashing clear water with droplets around the page edges"></div>
<div class="page"></div>

<header class="masthead abs">
  <div class="brand abs">Cedar Ridge Water District</div>
  <div class="tagline abs">Delivering Quality Water to Linden and Harlow Counties</div>
  <div class="phone abs">Ph: <span>(555) 014 2276</span></div>
  <div class="address abs">4870 Prairie Road, Maple Falls, Iowa 50999</div>
</header>

<ul class="nav abs">
  <li class="current">Home<svg width="24" height="30" viewBox="0 0 24 30"><rect width="24" height="30" fill="#0f4f9e"/><path d="M9 10l7 5-7 5z" fill="#fff"/></svg></li>
  <li>New Customer</li>
  <li>Resources</li>
  <li>Rates</li>
  <li>Rules and Regs</li>
  <li>Board and Staff</li>
  <li>Pay Online</li>
  <li>News</li>
  <li>Contact Us</li>
</ul>

<section class="slider abs">
  <div class="slide-photo" role="img" aria-label="Photo of a country road beside farm fields with a water tower"></div>
  <div class="slide-caption">
    <h2>Pure &amp; <span>Fresh Water!</span></h2>
    <p>Lorem ipsum dolor sit amet, consectetur adipiscing elit. Etiam mi purus, adipisci</p>
  </div>
  <div class="slide-bar">
    <span class="dot" style="left:13px;background:var(--lime)"></span>
    <span class="dot" style="left:25px"></span>
    <span class="dot" style="left:37px"></span>
  </div>
</section>

<aside class="facts abs">
  <h3>Water Facts!</h3>
  <p>Lorem ipsum dolor sit amet, consectetur adipi-scing elit. Etiam mi purus, adipiscing at ultrices a, gravida sed enim. Aenean at libero ac diam feugiat ornare. Integer ultricies dui</p>
</aside>

<aside class="member abs">
  <em>Proud Member of:</em>
  <div class="badge" style="left:18px;top:30px;width:90px;height:44px;border-radius:4px"></div>
  <div class="badge" style="left:132px;top:24px;width:34px;height:54px"></div>
</aside>

<main class="welcome abs">
  <h1>Welcome!</h1>
  <p>Lorem ipsum dolor sit amet, consectetur adipiscing elit. Etiam mi purus, adipiscing at ultrices a, gravida sed enim. Aenean at libero ac diam feugiat ornare. Integer ultricies dui vitae tellus vestibu-lum suscipit malesuada quam congue. Nullam non arcu urna, a congue enim. Curabitur egestas, diam non facilisis accumsan, libero justo tincidunt ante, ut pharetra ante urna ac nunc. Nam tincidunt vehicula nisi id ornare. In hac habitasse platea dictumst. Nulla gravida suscipit scelerisque. Vestibulum tempus mi at dui tristique ultrices.mare. In hac habitasse platea dictumst. Nulla gravida suscipit scelerisque. rnare. In hac habitasse platea dic-tumst. Nulla gravida suscipit scelerisque.</p>
  <p style="margin-top:16px">Proin viverra feugiat ante, vel porta eros varius eget. Duis pulvi-nar semper volutpat. Sed bibendum ullamcorper blandit. Etiam enim leo, cursus sit amet laoreet sit amet, pellentesque eu lacus. Curabitur nisl dui, hendrerit nec tincidunt at, lobortis nec enim. Donec felis diam, dignis</p>
</main>

<a class="btn btn-pay abs">Pay Bill Online</a>
<a class="btn btn-new abs">New Customers</a>

<section class="news abs">
  <h3>News &amp; Updates</h3>
  <div class="news-item tall">Lorem ipsum dolor sit amet-consectetur adipiscing elit.<time>07-May-2014 at Lorem</time></div>
  <div class="news-item short">Lorem ipsum dolor sit amet<time>07-May-2014 at Lorem</time></div>
  <div class="news-item">Lorem ipsum dolor sit amet<time>07-May-2014 at Lorem</time></div>
</section>
<a class="all-news abs">Click here to Read all News</a>

<footer class="footer abs">Cedar Ridge Water District &nbsp;|&nbsp; 4870 Prairie Road, Maple Falls, Iowa 50999 &nbsp;|&nbsp; (555) 014 2276 &nbsp;|&nbsp; www.cedarridgewater.example &nbsp;|&nbsp; Lorem Lipsum</footer>
</body>
</html>
```